An e-flyer for an exotic car and fine wine club.

This is the first meeting of Birchwell Motor Society and includes several businesses. Their logos should be featured at the bottom. It should be sleek, elegant and simple featuring a photo of an Corvane Lestrel R7 as well as my logo (I will provide photos). The flyer needs to look professional and appeal to billionaires.
The text should read:
Birchwell Motor society presents
Fast Cars and Fine Wine (but not while driving)
Hosted by Harlow Gem Vault
Bring your best car(s) and join us to enjoy the party with sommelier selected wines, the best classic and modern cars and hors d'oeuvre catered by Penrose's Clam House. Live DJ.
August 26th 3-6 p.m.
This event is gratis.
RSVP to dana@birchwellmotors.example for address and details

Target Market(s)
Very wealthy exotic car owners
Industry/Entity Type
Car Club, Fine Wines.
Requirements
Must have
- Style, panache, elegance, sleekness, simplicity. I like the idea of a black or dark flyer with a consistent color scheme.
Nice to have
- I want the flyer to be simple and sleek, feature an Corvane Lestrel R7 as the eye catcher, Birchwell Motor Society logo featured prominently on the top, and the other business logos on the bottom.
Should not have
- It must not be too noisy or busy.

```html
<!DOCTYPE html>
<html lang="en">
<head>
<meta charset="utf-8">
<title>Fast Cars and Fine Wine — Birchwell Motor Society</title>
<link rel="stylesheet" href="https://fonts.googleapis.com/css2?family=Inter:wght@400;500;600;700;800&family=Source+Serif+4:wght@500&display=swap">
<style>
  :root {
    --bg-top: #2a2b2f;
    --bg-mid: #2d2e32;
    --bg-low: #1f2023;
    --footer: #1c1d20;
    --white: #ffffff;
    --text: #f2f2f2;
    --gold: #f6cd7f;
    --rule-a: rgba(230, 110, 40, 0);
    --rule-b: #e2732f;
    --rule-c: #f2a04a;
    --car-a: #5b5e64;
    --car-b: #2c2e32;
  }
  * { margin: 0; padding: 0; box-sizing: border-box; }
  html, body { width: 848px; height: 1200px; overflow: hidden; background: var(--bg-low); }
  .flyer {
    position: relative;
    width: 848px;
    height: 1200px;
    overflow: hidden;
    background: linear-gradient(180deg, var(--bg-top) 0%, var(--bg-mid) 55%, var(--bg-low) 100%);
    font-family: "Inter", Arial, sans-serif;
    color: var(--text);
    text-align: center;
  }
  .club-mark {
    position: absolute;
    top: 58px; left: 0; width: 100%;
    display: flex; flex-direction: column; align-items: center; gap: 10px;
    color: var(--white);
    font-weight: 800;
    text-transform: uppercase;
  }
  .club-mark .dot { width: 38px; height: 38px; border-radius: 50%; background: var(--white); margin-bottom: 8px; }
  .club-mark .name-main { font-size: 46px; letter-spacing: 4px; line-height: 1; }
  .club-mark .name-sub { font-size: 20px; letter-spacing: 14px; line-height: 1; padding-left: 14px; }
  .presents {
    position: absolute; top: 258px; left: 0; width: 100%;
    font-size: 20px; font-weight: 600; letter-spacing: 5.2px; color: var(--white);
  }
  .rule {
    position: absolute; left: 89px; width: 670px; height: 2px;
    background: linear-gradient(90deg, var(--rule-a), var(--rule-b) 25%, var(--rule-c) 50%, var(--rule-b) 75%, var(--rule-a));
  }
  .rule.top { top: 304px; }
  .rule.bottom { top: 385px; }
  .title {
    position: absolute; top: 312px; left: 0; width: 100%;
    font-family: "Source Serif 4", Georgia, serif; font-weight: 500;
    font-size: 51px; line-height: 64px; color: var(--white);
  }
  .aside { position: absolute; top: 405px; left: 0; width: 100%; font-size: 28px; font-weight: 700; color: var(--white); }
  .host { position: absolute; top: 458px; left: 0; width: 100%; font-size: 22px; font-weight: 600; color: var(--white); }
  .details {
    position: absolute; top: 515px; left: 0; width: 100%;
    font-size: 17px; line-height: 22.5px; font-weight: 400; color: var(--text);
  }
  .date { position: absolute; top: 614px; left: 0; width: 100%; font-size: 28px; font-weight: 700; color: var(--gold); }
  .price { position: absolute; top: 670px; left: 0; width: 100%; font-size: 22px; font-weight: 600; color: var(--white); }
  .rsvp { position: absolute; top: 710px; left: 0; width: 100%; font-size: 17px; font-weight: 600; color: var(--white); }
  .hero-car {
    position: absolute; top: 772px; left: 168px; width: 594px; height: 296px;
    border-radius: 46% 54% 18% 22% / 50% 50% 24% 24%;
    background: radial-gradient(ellipse at 55% 35%, var(--car-a) 0%, var(--car-b) 80%);
  }
  .partners {
    position: absolute; bottom: 0; left: 0; width: 100%; height: 109px;
    background: var(--footer);
    display: flex; align-items: center; justify-content: center; gap: 44px;
    font-size: 20px; font-weight: 700; color: var(--white); text-transform: uppercase; letter-spacing: 1px;
  }
  .partner { display: flex; align-items: center; gap: 8px; }
  .partner .square { width: 14px; height: 14px; background: var(--white); }
</style>
</head>
<body>
  <main class="flyer">
    <header class="club-mark" aria-label="Birchwell Motor Society">
      <span class="dot"></span>
      <span class="name-main">Birchwell</span>
      <span class="name-sub">Motor Society</span>
    </header>

    <p class="presents">BIRCHWELL MOTOR SOCIETY PRESENTS</p>
    <div class="rule top"></div>
    <h1 class="title">Fast Cars and Fine Wine</h1>
    <div class="rule bottom"></div>
    <p class="aside">(but not while driving)</p>
    <p class="host">Hosted by Harlow Gem Vault</p>
    <p class="details">Bring your best car(s) and join us to enjoy the party with<br>sommelier selected wines, the best classic and modern cars<br>and hors d'oeuvre catered by Penrose's Clam House. Live DJ.</p>
    <p class="date">August 26th 3-6 p.m.</p>
    <p class="price">This event is gratis.</p>
    <p class="rsvp">RSVP to dana@birchwellmotors.example for address and details</p>

    <div class="hero-car" role="img" aria-label="Photo of a dark grey Corvane Lestrel R7 classic coupe"></div>

    <footer class="partners">
      <span class="partner">Marlowe Cellars</span>
      <span class="partner"><span class="square"></span>Harlow Gem Vault</span>
    </footer>
  </main>
</body>
</html>
```